KESTRELMAR NAUTICA SUPPLIERS SELL SHEETS

Create a group of Sell Sheets that can be used in client meetings and willbe incorporated into web site pages in the future. We wish to highlight our Mission Statement / Company Bio / Services and Products offered. This piece may be 8 to 12 pages. In the near future this will grow to include an on-line Catalog with 300 to 500 pages of product offerings.

It will not list individual products and prices but rather will serve as a New Business introduction using brief descriptive text and a lot of industry photos. At this time we do have a Logo and Tag Line which will be used.

The image we need to portray is High End Quality Sales, Service, Professional Industry Experience and Reliability. My personal experience includes 27 years as a ship´s Captain working all over the world.

We are a start-up Ship´s Chandler service, located in Macae, Brasil. We will sell products and inspection services to the Offshore Petroleum Industry which includes vessels and platforms. These products will include the simple monthly supply replenishment (like paper towels / laundry soap / drinking water) to the more technical, like Pop Off Valves (sales & inspection certifications), Transfer Hoses, Sales Service and Certifications, OEM Filters for Engines& Generators, Anchor Harware, Nautical Bulbs & Light Fixtures Safety Gear and hundreds of other items.

We will have a group of EMERGENCY GEAR on-hand in our warehouse, to supply in cases like a lost anchor for example. We willoffer a Guaranteed 30 hour delivery anywhere in Brasil. These vessels work at a rate of up to $50K per day and cannot afford what is called`Down Time` or time off the clock.

All text will be supplied in both English and Portuguese. I prefer that each block of text will show both languages with a distinctive color or typeface for each. Please present your ideas on how to deal with the two languages.

Sorry for any mis-spellings but today I am forced to work on a Portuguese keyboard.

Target Market(s)

Ship´s Captains, Purchasing Managers, Company Directors, Engineers

Industry/Entity Type

Business

Requirements
Must have
• I am open to a Professional, High End look. I would like to incorporate photos and ``historical`` illustrations to tella story, which I will supply.

I have attached our new Company Logo which has the tag line....``TO STAY THE COURSE´´. We would like to repeat the logo and tag line whenever possible without being too obnoxious.

```html
<!DOCTYPE html>
<html lang="en">
<head>
<meta charset="utf-8">
<title>Kestrelmar Nautica Suppliers — Sell Sheet</title>
<link href="https://fonts.googleapis.com/css2?family=Montserrat:wght@700&family=Carlito:ital,wght@0,400;0,700;1,400;1,700&display=swap" rel="stylesheet">
<style>
  :root {
    --gold: #f5c518;
    --green: #1b5e33;
    --ink: #111111;
    --grey-text: #6b6b6b;
    --orange: #e4996c;
    --taupe: #958a86;
    --amber: #fec537;
    --white: #ffffff;
  }
  * { margin: 0; padding: 0; box-sizing: border-box; }
  html, body { width: 927px; height: 1200px; overflow: hidden; background: var(--white); }
  .sheet {
    position: relative; width: 927px; height: 1200px;
    font-family: "Carlito", "Calibri", sans-serif; color: var(--ink);
  }
  .masthead {
    position: absolute; top: 52px; left: 0; width: 927px; text-align: center;
    font-family: "Montserrat", "Century Gothic", sans-serif; font-weight: 700;
    font-size: 44px; letter-spacing: 0.5px; color: var(--gold);
  }
  .masthead .accent { color: var(--green); }
  .intro {
    position: absolute; top: 174px; width: 262px;
    font-size: 16px; line-height: 21.5px;
  }
  .intro--en { left: 64px; color: var(--ink); }
  .intro--pt { left: 359px; width: 282px; color: var(--grey-text); }
  .hero-photo {
    position: absolute; left: 662px; top: 188px; width: 222px; height: 240px;
    border-radius: 50%;
    background: radial-gradient(circle at 45% 45%, #d8b04a 0%, #a88428 45%, #f4eddc 72%, #ffffff 100%);
  }
  .tagline {
    position: absolute; top: 500px; left: 0; width: 927px; text-align: center;
    font-style: italic; font-weight: 700; font-size: 32px; color: var(--green);
  }
  .service {
    position: absolute; top: 587px; width: 259px; height: 259px; padding: 12px 11px;
    box-shadow: 5px 6px 7px rgba(0,0,0,0.45);
  }
  .service h2 { font-weight: 700; font-size: 21.5px; line-height: 29px; color: var(--white); }
  .service p { font-style: italic; font-size: 13px; line-height: 18px; margin-top: 4px; color: var(--ink); }
  .service--supply { left: 46px; background: var(--orange); }
  .service--technical { left: 336px; background: var(--taupe); }
  .service--emergency { left: 626px; background: var(--amber); }
  .detail {
    position: absolute; top: 912px; width: 245px;
    font-style: italic; font-size: 14.5px; line-height: 20px;
  }
  .detail--en { left: 54px; color: var(--ink); }
  .detail--pt { left: 326px; color: var(--grey-text); }
  .brand-mark {
    position: absolute; left: 602px; top: 945px; width: 295px; height: 210px;
    display: flex; flex-direction: column; align-items: center; justify-content: center; gap: 14px;
  }
  .brand-mark .dot { width: 60px; height: 60px; border-radius: 50%; background: var(--gold); }
  .brand-mark .name { font-weight: 700; font-size: 19px; color: var(--green); text-align: center; }
  .footer {
    position: absolute; top: 1120px; left: 40px; width: 510px; text-align: center;
    font-style: italic; font-size: 16px; line-height: 21px;
  }
</style>
</head>
<body>
<main class="sheet">
  <h1 class="masthead">KESTRELMAR <span class="accent">NAUTICA</span> SUPPLIERS</h1>

  <p class="intro intro--en">High-end sales and service, extensive industry experience, reliability.From Macae, Brasil, we offer products and inspection services to the Offshore Petroleum Industry. Large or small, routine or emergency, we have you covered. We understand the seriousness of surprise downtime, and work to fulfil the unexpected needs of our clients, supplying lost or damaged equipment within thirty hours, guaranteed.</p>

  <p class="intro intro--pt" lang="pt">Alta qualidade de vendas e serviços, ampla experiência da indústria, confiabilidade. De Macaé, Brasil, oferecemos produtos e serviços de inspeção para a Indústria de Petróleo Offshore. Grande ou pequena rotina, ou de emergência, temos que cobertas. Entendemos a gravidade da paralisação surpresa, e trabalhar para satisfazer as necessidades inesperadas de nossos clientes, fornecendo perdido ou danificado equipamento dentro 30 horas, garantido.</p>

  <div class="hero-photo" role="img" aria-label="Photo of a brass ship's wheel"></div>

  <p class="tagline">“TO STAY THE COURSE”</p>

  <section class="service service--supply">
    <h2>Monthly Supply &amp; Replenishment –</h2>
    <p>Keep on top of your day-to-day needs</p>
  </section>
  <section class="service service--technical">
    <h2>Technical &amp; Specialty Equipment</h2>
    <p>A wide array of nautical hardware</p>
  </section>
  <section class="service service--emergency">
    <h2>Emergency Gear – Guaranteed Delivery</h2>
    <p>Within thirty hours, replacements for lost or damaged equipment</p>
  </section>

  <p class="detail detail--en">Lorem Ipsum is simply dummy text of the printing and typesetting industry. Lorem Ipsum has been the industry’s standard dummy text ever since the 1500s, when an unknown printer took a galley of type and scrambled it to make...</p>
  <p class="detail detail--pt" lang="pt">O Lorem Ipsum é um texto modelo da indústria tipográfica e de impressão. O Lorem Ipsum tem vindo a ser o texto padrão usado por estas indústrias desde o ano de 1500, quando uma misturou os caracteres de um texto...</p>

  <div class="brand-mark">
    <span class="dot"></span>
    <span class="name">KESTRELMAR NAUTICA SUPPLIERS</span>
  </div>

  <footer class="footer">
    contact information • contact information • contact info<br>
    legal info, boilerplate footer material et cetera
  </footer>
</main>
</body>
</html>
```